Stationery Required - Own Logo provided

Hi,

We are a retail company called 'Copperfinch Trading Limited' based in the UK and would like some corporate stationery designed.

We have provided our Logo which we would like to use (Its attached to this brief)...

The designs must be orginal, professional, stylish and interesting!

Target Market(s)

We will use this stationery to communicate with our wholesale suppliers and employees, so it must have a 'professional' feel about it.

Industry/Entity Type

It Company

Requirements
Must have
• Must be professional, corporate, stylish and not to 'fussy'. we require ... Business card design, a4 letter, compliment slip. All designs must be supplied in a format where the text (address/telephone numbers etc..) can be edited, as we have alot of staff and operate out of several different premises.
Nice to have
• I would like a windows backround picture file supplied as well so we can integrate that onto our computer systems.

```html
<!DOCTYPE html>
<html lang="en">
<head>
<meta charset="utf-8">
<title>Copperfinch Trading Limited — Stationery</title>
<link href="https://fonts.googleapis.com/css2?family=Questrial&family=Open+Sans:wght@700&display=swap" rel="stylesheet">
<style>
  :root {
    --lime: #84ff12;
    --lime-soft: #c9f7a0;
    --forest: #2f5a0e;
    --panel: #2e3438;
    --paper: #ffffff;
    --shadow: rgba(0,0,0,0.35);
  }
  * { margin: 0; padding: 0; box-sizing: border-box; }
  html, body { width: 1200px; height: 849px; overflow: hidden; background: var(--paper); }
  body { position: relative; font-family: "Questrial", sans-serif; color: var(--forest); }

  .brand-header {
    position: absolute; left: 0; top: 0; width: 1200px; height: 235px;
    display: flex; align-items: center; justify-content: center; gap: 22px;
  }
  .brand-header .brand-square { width: 92px; height: 92px; background: var(--forest); }
  .brand-header .brand-name { font-size: 58px; color: var(--forest); letter-spacing: 0.5px; }

  .display-panel { position: absolute; left: 0; top: 235px; width: 1200px; height: 578px; background: var(--panel); }
  .base-band { position: absolute; left: 0; top: 815px; width: 1200px; height: 26px; background: var(--lime); }

  .sheet { position: absolute; background: var(--paper); overflow: hidden; box-shadow: 2px 3px 6px var(--shadow); }
  .band { position: absolute; left: 0; right: 0; bottom: 0; background: var(--lime); }
  .mini-brand { position: absolute; display: flex; align-items: center; gap: 5px; color: var(--forest); white-space: nowrap; }
  .mini-brand .brand-square { background: var(--forest); flex: none; }
  .contact { position: absolute; text-align: right; font-size: 7.5px; line-height: 1.25; color: var(--forest); white-space: nowrap; }

  /* compliment slip */
  .compliment-slip { left: 54px; top: 313px; width: 216px; height: 412px; }
  .compliment-slip .band { height: 110px; }
  .compliment-slip .greeting {
    position: absolute; left: 214px; top: 6px; font-size: 8.5px; color: var(--forest);
    transform: rotate(90deg); transform-origin: left top; white-space: nowrap;
  }
  .compliment-slip .mini-brand {
    left: 30px; bottom: 6px; transform: rotate(-90deg); transform-origin: left bottom;
    color: var(--paper); font-size: 9px; line-height: 1.15; gap: 5px;
  }
  .compliment-slip .mini-brand .brand-square { width: 14px; height: 14px; background: var(--paper); }
  .compliment-slip .accent-square { position: absolute; right: 0; bottom: 110px; width: 60px; height: 36px; background: var(--lime); }

  /* business card front */
  .card-front { left: 349px; top: 313px; width: 384px; height: 206px; }
  .card-front .band { height: 26px; }
  .card-front .mini-brand { left: 9px; top: 12px; font-size: 15px; }
  .card-front .mini-brand .brand-square { width: 15px; height: 15px; }
  .card-front .holder { position: absolute; left: 161px; top: 90px; font-family: "Open Sans", sans-serif; font-weight: 700; font-size: 12px; line-height: 1.3; color: var(--forest); }
  .card-front .contact { right: 4px; top: 151px; }

  /* business card back */
  .card-back { left: 350px; top: 543px; width: 385px; height: 205px; }
  .card-back .band { height: 28px; }
  .card-back .mini-brand { left: 0; right: 0; top: 70px; justify-content: center; font-size: 22px; gap: 10px; }
  .card-back .mini-brand .brand-square { width: 22px; height: 22px; }

  /* letterhead */
  .letterhead { left: 808px; top: 279px; width: 349px; height: 501px; }
  .letterhead .band { height: 23px; }
  .letterhead .mini-brand { left: 7px; top: 10px; font-size: 12px; }
  .letterhead .mini-brand .brand-square { width: 12px; height: 12px; }
  .letterhead .contact { right: 4px; top: 7px; font-size: 8px; }
  .letterhead .faint-square { position: absolute; right: 0; bottom: 23px; width: 165px; height: 165px; background: var(--lime-soft); opacity: 0.8; }
</style>
</head>
<body>
  <header class="brand-header">
    <span class="brand-square"></span>
    <span class="brand-name">Copperfinch Trading Limited</span>
  </header>

  <div class="display-panel"></div>
  <div class="base-band"></div>

  <section class="sheet compliment-slip">
    <span class="greeting">With Compliments</span>
    <span class="accent-square"></span>
    <div class="band"></div>
    <div class="mini-brand"><span class="brand-square"></span><span>Copperfinch Trading<br>Limited</span></div>
  </section>

  <section class="sheet card-front">
    <div class="mini-brand"><span class="brand-square"></span>Copperfinch Trading Limited</div>
    <div class="holder">Name<br>Designation</div>
    <div class="contact">Unit 48, Harlow Yard<br>Phone: 020-555-0143<br>Email: hello@copperfinch.co.uk</div>
    <div class="band"></div>
  </section>

  <section class="sheet card-back">
    <div class="mini-brand"><span class="brand-square"></span>Copperfinch Trading Limited</div>
    <div class="band"></div>
  </section>

  <section class="sheet letterhead">
    <div class="mini-brand"><span class="brand-square"></span>Copperfinch Trading Limited</div>
    <div class="contact">Unit 48, Harlow Yard<br>Phone: 020-555-0143<br>Email: hello@copperfinch.co.uk</div>
    <span class="faint-square"></span>
    <div class="band"></div>
  </section>
</body>
</html>
```